Corporate car (wrap) for maintenance services company

Hello,

We would like to design our corporate cars (wraps), for maintenance services company. the company specializes in providing maintenance to residential properties.

The company name is "Harbor gold services"

Website: WWW.HGS-Firmline.com

We will receive all the cars in WHITE color

Design specifications:
1. Simple design
2. Two colors only ( white and blue) as per the logo (attached)
3. Customer service toll free # should be added which is 9300 48261
4. website should be mentioned : www.HGS-Firmline.com
5. the slogan should be mentioned " Convenient maintenance solutions"
6. Logo should clearly appear in more than one side of the car.
7. the final design should communicate to homeowners that we provide maintenance services to their homes.
8. Please use the Mac type font. ,as per the logo
9. Please include the back of the car in the design.

Attachements:
1. Logo
2. Car brochure
3. Pictures of the cars

There must be a 3D picture of the design.

• 3D picture of the final design, logo, website, customer service phone # & slogan, all should appear in the sticker.

```html
<!DOCTYPE html>
<html lang="en">
<head>
<meta charset="utf-8">
<title>Harbor gold services – vehicle wrap</title>
<link href="https://fonts.googleapis.com/css2?family=Audiowide&display=swap" rel="stylesheet">
<style>
  :root {
    --wrap-base: #eceef0;
    --brand-blue: #1b6fae;
    --brand-blue-deep: #14578b;
    --brand-white: #ffffff;
  }
  html, body {
    margin: 0;
    padding: 0;
    width: 1200px;
    height: 600px;
    overflow: hidden;
    background: var(--wrap-base);
  }
  .wrap-canvas {
    position: relative;
    width: 1200px;
    height: 600px;
    font-family: "Audiowide", sans-serif;
  }
  .wrap-graphics {
    position: absolute;
    inset: 0;
  }
  .band { fill: var(--brand-blue); }
  .band-deep { fill: var(--brand-blue-deep); }
  .slogan {
    fill: var(--brand-white);
    font-size: 36px;
    letter-spacing: 2px;
  }
  .tollfree {
    fill: var(--brand-white);
    font-size: 23px;
    letter-spacing: 1px;
  }
  .website {
    fill: var(--brand-blue);
    font-size: 21px;
    letter-spacing: 1px;
  }
  .brand-mark {
    position: absolute;
    left: 150px;
    top: 250px;
    display: flex;
    align-items: center;
    gap: 12px;
    color: var(--brand-blue);
    font-family: "Audiowide", sans-serif;
    font-weight: 400;
    font-size: 26px;
  }
  .brand-mark__square {
    width: 34px;
    height: 34px;
    background: var(--brand-blue);
    flex: none;
  }
</style>
</head>
<body>
<main class="wrap-canvas">
  <svg class="wrap-graphics" viewBox="0 0 1200 600" width="1200" height="600">
    <polygon class="band-deep" points="560,360 1200,200 1200,208 560,368"/>
    <polygon class="band" points="420,400 1200,220 1200,300 900,360"/>
    <polygon class="band" points="120,520 1200,315 1200,385 120,590"/>
    <polygon class="band-deep" points="450,600 1200,450 1200,600"/>
    <text class="tollfree" x="1000" y="306" text-anchor="middle" transform="rotate(-12 1000 306)">toll free 9300 48261</text>
    <text class="slogan" x="640" y="468" text-anchor="middle" transform="rotate(-10.8 640 468)">CONVENIENT MAINTENANCE SOLUTIONS</text>
    <text class="website" x="720" y="527" text-anchor="middle" transform="rotate(-10.8 720 527)">www.hgs-firmline.com</text>
  </svg>

  <div class="brand-mark">
    <span class="brand-mark__square"></span>
    <span class="brand-mark__name">Harbor gold services</span>
  </div>
</main>
</body>
</html>
```